Kelbrook Tutoring Flyer Design

I need a flyer for a new company based in Samford Valley called 'Kelbrook Tutoring'. We specialise in Mathematics tutoring for students from grade 5 up to grade twelve. We currently have a logo that has purple as its major colour. The final design should convey professionalism, compassion and that education is about maximising peoples possibilities,
Updates

Just thought I would let you know that my slogan is "Maximise your possibilities" and my phone number is 0438260917

Thanks.

My current logo doesn't seem to want to upload

Target Market(s)

The two targets are parents of students in grades 5-12 and students in grades 5-12

Industry/Entity Type

Education

Logo Text

Kelbrook Tutoring

Logo styles of interest
Pictorial/Combination Logo
Abstract Logo
Lettermark Logo
Requirements
Must have
• My slogan is "Maximise your possibilities"
my phone number is 0438260917

```html
<!DOCTYPE html>
<html lang="en">
<head>
<meta charset="utf-8">
<title>Kelbrook Tutoring Flyer Design</title>
<link rel="stylesheet" href="https://fonts.googleapis.com/css2?family=Italianno&family=Kalam:wght@700&family=Libre+Franklin:wght@400;700&family=Crimson+Text&display=swap">
<style>
  :root {
    --violet-deep: #622a87;
    --violet-mid: #7b3a9e;
    --violet-soft: #a45bbf;
    --rose: #e8507f;
    --blush: #f6c6dc;
    --rule: #a866c0;
    --leaf-soft: rgba(140, 198, 63, 0.55);
    --white: #ffffff;
  }
  * { margin: 0; padding: 0; box-sizing: border-box; }
  html, body { width: 933px; height: 1200px; overflow: hidden; background: var(--violet-deep); }
  .flyer {
    position: relative;
    width: 933px;
    height: 1200px;
    overflow: hidden;
    background: var(--violet-deep);
    color: var(--white);
  }
  .hero-backdrop {
    position: absolute;
    left: 0; top: 0;
    width: 933px; height: 680px;
    background:
      radial-gradient(ellipse 420px 260px at 420px 360px, rgba(255,255,255,0.22), transparent 70%),
      radial-gradient(ellipse 500px 300px at 90px 60px, rgba(255,235,245,0.85), transparent 70%),
      radial-gradient(ellipse 360px 420px at 30px 420px, rgba(232,80,127,0.85), transparent 70%),
      linear-gradient(180deg, var(--violet-soft) 0%, var(--violet-mid) 55%, var(--violet-deep) 96%);
  }
  .logo-box {
    position: absolute;
    left: 24px; top: 28px;
    width: 154px; height: 66px;
    background: var(--violet-mid);
    border: 2px solid var(--blush);
    border-radius: 4px;
    display: flex; align-items: center; justify-content: center;
    font-family: 'Libre Franklin', sans-serif;
    font-weight: 700;
    font-size: 22px;
  }
  .brand-title {
    position: absolute;
    left: 0; top: 535px;
    width: 933px;
    text-align: center;
    font-family: 'Italianno', cursive;
    font-weight: 400;
    font-size: 126px;
    line-height: 1;
  }
  .slogan {
    position: absolute;
    left: 0; top: 710px;
    width: 933px;
    text-align: center;
    font-family: 'Kalam', cursive;
    font-weight: 700;
    font-size: 43px;
  }
  .service-note {
    position: absolute;
    left: 0; top: 810px;
    width: 933px;
    text-align: center;
    font-family: 'Libre Franklin', sans-serif;
    font-size: 23px;
    line-height: 37px;
  }
  .supplies-art {
    position: absolute;
    left: 430px; top: 914px;
    width: 92px; height: 174px;
    border-radius: 14px;
    background: radial-gradient(ellipse 60% 55% at 50% 60%, var(--leaf-soft), transparent 100%);
  }
  .footer-rule {
    position: absolute;
    left: 0; top: 1107px;
    width: 933px; height: 2px;
    background: var(--rule);
  }
  .contact-line {
    position: absolute;
    left: 0; top: 1134px;
    width: 933px;
    text-align: center;
    font-family: 'Crimson Text', serif;
    font-size: 25px;
  }
</style>
</head>
<body>
  <main class="flyer">
    <div class="hero-backdrop" role="img" aria-label="Abstract pink and purple light rays with glowing bokeh circles"></div>
    <div class="logo-box">Your Logo</div>
    <h1 class="brand-title">Kelbrook Tutoring</h1>
    <p class="slogan">Maximise your possibilities</p>
    <p class="service-note">We specialise in Mathematics tutoring for<br>students from grade five up to grade twelve</p>
    <div class="supplies-art" role="img" aria-label="Illustration of a pencil holder with coloured pencils"></div>
    <div class="footer-rule"></div>
    <p class="contact-line">Call : 0438260917</p>
  </main>
</body>
</html>
```